Self help book from Bright Harbor needs awesome cover

We need a paperback and e-book cover for a self help book that is about to be published. The title is 'Silver Compass Calls Traveler: Shape Restless Hunger Toward Splendor'. Synopsis: Future You has achieved great success, and is trying to get an urgent communication to Present You to tell you how to master your mind and life so that you can achieve that greatness. If you don’t, the future won’t happen like it can, or should. Your destiny is to really make a difference in the lives of all of us. It’s not just for you. There are practical things you can do to think more clearly, and some mindfulness exercises to hone your skills. We currently do not have any color or graphic preferences, we're excited to see what you come up with! The final cover should express clarity, confidence, and a bit of urgency. Author's name is Glen Marlow. Author name should be at the bottom.

```html
<!DOCTYPE html>
<html lang="en">
<head>
<meta charset="UTF-8">
<title>Silver Compass Calls Traveler – Cover</title>
<link href="https://fonts.googleapis.com/css2?family=Bebas+Neue&family=Crimson+Text&display=swap" rel="stylesheet">
<style>
  :root {
    --stage: #f4f4f4;
    --stage-edge: #e6e6e6;
    --ink: #0a0806;
    --wood-top: #5a2c12;
    --wood-mid: #8a4a1c;
    --amber: #c98a34;
    --glow: #fff4d2;
    --ground: #120d09;
  }
  * { margin: 0; padding: 0; box-sizing: border-box; }
  html, body {
    width: 1200px;
    height: 800px;
    overflow: hidden;
  }
  body {
    background: radial-gradient(ellipse at 50% 45%, var(--stage) 40%, var(--stage-edge) 100%);
    position: relative;
  }
  .book-cover {
    position: absolute;
    left: 382px;
    top: 40px;
    width: 436px;
    height: 720px;
    overflow: hidden;
    box-shadow: 0 10px 30px rgba(0, 0, 0, 0.18);
  }
  .cover-scene {
    position: absolute;
    inset: 0;
    width: 100%;
    height: 100%;
  }
  .cover-title {
    position: absolute;
    left: 0;
    right: 0;
    top: 128px;
    text-align: center;
    font-family: "Bebas Neue", sans-serif;
    font-weight: 400;
    color: var(--ink);
    line-height: 0.83;
  }
  .cover-title .line {
    display: block;
    font-size: 80px;
    letter-spacing: 0.5px;
  }
  .cover-title .line-lead {
    font-size: 104px;
  }
  .cover-subtitle {
    position: absolute;
    left: 30px;
    right: 30px;
    top: 392px;
    text-align: center;
    font-family: "Crimson Text", serif;
    font-size: 22px;
    line-height: 1.3;
    color: var(--ink);
  }
  .cover-author {
    position: absolute;
    left: 0;
    right: 0;
    bottom: 18px;
    text-align: center;
    font-family: "Crimson Text", serif;
    font-size: 24px;
    letter-spacing: 2px;
    color: var(--glow);
  }
</style>
</head>
<body>
  <div class="book-cover">
    <svg class="cover-scene" viewBox="0 0 436 720" role="img" aria-label="Photo of a person in silhouette with arms raised, standing in a sunlit stone arcade filled with golden light and mist">
      <defs>
        <linearGradient id="sceneBase" x1="0" y1="0" x2="0" y2="1">
          <stop offset="0" stop-color="var(--wood-top)"/>
          <stop offset="0.18" stop-color="var(--wood-mid)"/>
          <stop offset="0.45" stop-color="var(--amber)"/>
          <stop offset="0.8" stop-color="#b98650"/>
          <stop offset="1" stop-color="#6b4a33"/>
        </linearGradient>
        <radialGradient id="sceneGlow" cx="0.4" cy="0.5" r="0.45">
          <stop offset="0" stop-color="var(--glow)" stop-opacity="1"/>
          <stop offset="0.4" stop-color="#f6d48a" stop-opacity="0.75"/>
          <stop offset="1" stop-color="#f6d48a" stop-opacity="0"/>
        </radialGradient>
      </defs>
      <rect width="436" height="720" fill="url(#sceneBase)"/>
      <rect width="436" height="720" fill="url(#sceneGlow)"/>
      <path d="M0 650 L60 655 L140 660 L230 668 L320 664 L436 670 L436 720 L0 720 Z" fill="var(--ground)"/>
    </svg>

    <h1 class="cover-title">
      <span class="line">Silver</span>
      <span class="line">Compass Calls</span>
      <span class="line line-lead">Traveler</span>
    </h1>

    <p class="cover-subtitle">Shape Restless Hunger Toward<br>Splendor</p>

    <p class="cover-author">Glen Marlow</p>
  </div>
</body>
</html>
```